Healthy Meal Delivery Website Needs to be updated, current, fresh and modern

Hi there,

The current website i have is super old and outdated.

I would like a beautiful modern site that has all the same content as the previous except with a a new, modern and trustworthy feel.

The current website is https://velmorplatekitchen.com/

Target Market(s)

Health Conscious Young Professionals

Industry/Entity Type

Food Service

Font styles to use
Sans Serif

Requirements
Must have
• Modern Trustworthy feel
Should not have
• Anything out dated or cheesy or scammy

```html
<!DOCTYPE html>
<html lang="en">
<head>
<meta charset="utf-8">
<title>Velmor Plate Kitchen</title>
<link rel="stylesheet" href="https://fonts.googleapis.com/css2?family=Comic+Neue:wght@400;700&family=Lato:wght@400;700&display=swap">
<style>
:root{
  --blue:#1a9fd8;
  --blue-dark:#1389bd;
  --yellow:#f1e31c;
  --ink:#333;
  --muted:#666;
  --dark:#2a2522;
  --card:#f3f3f3;
  --line:#d8d8d8;
  --white:#fff;
}
*{box-sizing:border-box;margin:0;padding:0}
html,body{width:1200px;height:3358px;overflow:hidden}
body{font-family:"Lato",sans-serif;color:var(--ink);background:var(--white);position:relative}
.display{font-family:"Comic Neue",sans-serif;font-weight:700}
section,header,footer{position:absolute;left:0;width:1200px}

/* hero */
.hero{top:0;height:660px;background:radial-gradient(ellipse at 60% 55%,#7d8b4a 0%,#55603a 30%,#3d3a30 60%,#2c2a27 100%)}
.topbar{position:absolute;top:0;left:0;width:1200px;height:70px;display:flex;align-items:center;padding:0 120px}
.menu-icon{width:26px;height:20px;display:flex;flex-direction:column;justify-content:space-between}
.menu-icon span{height:3px;background:var(--white);border-radius:2px}
.brand{position:absolute;left:460px;top:20px;display:flex;align-items:center;gap:10px}
.brand-mark{width:22px;height:22px;background:var(--yellow)}
.brand-name{font-family:"Lato",sans-serif;font-weight:700;font-size:20px;color:var(--yellow)}
.top-actions{position:absolute;right:130px;top:24px;display:flex;gap:26px;align-items:center;color:var(--white);font-size:13px}
.hero-title{position:absolute;top:278px;width:100%;text-align:center;color:var(--white);font-size:54px}
.hero-sub{position:absolute;top:340px;left:355px;width:490px;text-align:center;color:var(--white);font-size:13px;line-height:1.45}
.btn-yellow{background:var(--yellow);color:var(--ink);font-size:13px;border-radius:5px;display:inline-block;text-align:center}
.hero .btn-yellow{position:absolute;left:531px;top:398px;width:140px;height:32px;line-height:32px}
.arrows{position:absolute;display:flex;gap:40px}
.dots{position:absolute;display:flex;flex-direction:column;gap:14px}
.dots i{width:11px;height:11px;border:2px solid var(--white);border-radius:50%;display:block}
.dots i.on{width:22px;height:4px;border:0;border-radius:2px;background:var(--blue);margin-left:-10px}

/* features band */
.features{top:660px;height:135px;background:var(--blue);display:flex}
.feature{flex:1;display:flex;align-items:center;justify-content:center;gap:14px;color:var(--white)}
.feature.mid{background:var(--blue-dark)}
.feature strong{display:block;font-size:15px}
.feature small{font-size:11px}

/* intro */
.intro{top:795px;height:519px;text-align:center}
.section-title{color:var(--blue);font-size:31px;line-height:1.1}
.intro .section-title{margin-top:58px}
.section-lead{font-size:12px;color:var(--muted);line-height:1.5;margin:18px auto 0;width:640px}
.cards{position:absolute;top:205px;left:123px;display:flex;gap:27px}
.card{width:217px;height:243px;background:var(--card);border-radius:6px;padding:22px 26px 0;position:relative;font-size:11px;color:var(--muted)}
.card.active{background:var(--yellow);color:var(--ink)}
.card h3{font-size:11px;font-weight:400;letter-spacing:.5px;margin:8px 0 14px}
.card p{line-height:1.45}
.card .more{position:absolute;bottom:18px;left:0;width:100%;font-size:11px}

/* menu */
.menu{top:1314px;height:428px;background:linear-gradient(180deg,#3a2e28,#2a2522);text-align:center;color:var(--white)}
.menu .section-title{color:var(--white);margin-top:62px;font-size:30px;font-weight:400}
.menu .section-lead{color:#eee;width:700px}
.dishes{position:absolute;top:186px;left:0;display:flex}
.dish{width:300px;height:242px;position:relative}
.dish .label{position:absolute;bottom:18px;width:100%;text-align:center}
.dish .label b{display:block;font-family:"Comic Neue",sans-serif;font-size:30px;font-weight:400}
.dish .label span{font-size:11px}
.dish-d{background:linear-gradient(135deg,#5a4632,#3b2e24)}
.dish-b{background:linear-gradient(135deg,#6b6a66,#3a3834)}
.dish-l{background:linear-gradient(135deg,#8aa35a,#c7c2a6)}
.dish-s{background:linear-gradient(135deg,#7c3a5a,#b35a4a)}
.dish-s .label{top:70px;bottom:auto}
.slide-arrow{position:absolute;top:271px}

/* plan */
.plan{top:1742px;height:560px}
.plan .section-title{text-align:center;margin-top:58px}
.plan .section-lead{text-align:center;margin-top:10px}
.faq{position:absolute;left:123px;top:150px;width:460px}
.faq-item{border-bottom:1px solid var(--line);padding:8px 0 12px}
.faq-item h4{color:var(--blue);font-size:12px;font-weight:400;letter-spacing:.4px;margin-bottom:6px}
.faq-item p{font-size:11px;color:var(--muted);line-height:1.45}
.veg{position:absolute;left:640px;top:130px;width:560px;height:380px;background:radial-gradient(ellipse at 55% 55%,#d83a22 0%,#e07a1f 30%,#6d3a6a 55%,rgba(255,255,255,0) 75%)}

/* testimonials */
.reviews{top:2302px;height:430px;background:radial-gradient(ellipse at 50% 50%,#3a312c,#221d1a);color:var(--white);text-align:center}
.reviews .section-title{color:var(--white);font-weight:400;margin-top:52px;font-size:30px}
.quote{position:absolute;left:290px;top:170px;width:620px;font-size:12px;line-height:1.5;text-align:center}
.quote-mark{position:absolute;left:248px;top:160px;font-size:48px;font-family:"Comic Neue",sans-serif}
.author{position:absolute;top:252px;width:100%;font-size:16px;font-weight:400}

/* newsletter */
.newsletter{top:2732px;height:324px;text-align:center}
.newsletter .section-title{margin-top:70px}
.newsletter .section-lead{width:700px}
.signup{position:absolute;left:318px;top:202px;display:flex;gap:12px}
.signup .field{width:468px;height:40px;border:1px solid var(--line);border-radius:4px;font-size:11px;color:#aaa;text-align:left;padding:12px 14px}
.signup .btn-yellow{width:100px;height:40px;line-height:40px;color:var(--blue)}

/* footer */
.footer{top:3056px;height:302px;background:var(--dark);color:var(--white)}
.fcol{position:absolute;top:52px;font-size:11px;line-height:1.7}
.fcol h5{font-family:"Comic Neue",sans-serif;color:var(--yellow);font-size:19px;font-weight:700;margin-bottom:12px;line-height:1.2}
.fcol.about{left:636px;width:205px;line-height:1.4}
.contact-row{display:flex;gap:12px;align-items:center}
.social{display:flex;gap:24px;margin-top:10px}
.social i{width:14px;height:14px;border-radius:50%;background:var(--white);display:block}
.like{display:flex;gap:6px;margin-top:12px}
.like i{width:54px;height:20px;background:#4a67ad;border-radius:3px;display:block}
.like i+i{width:40px}
.qform{display:grid;grid-template-columns:100px 100px;gap:6px}
.qform div{border:1px solid var(--white);height:20px;font-size:10px;padding:2px 4px;line-height:1.4}
.qform .msg{grid-column:span 2;height:68px}
.qform .send{width:94px;background:var(--yellow);color:var(--blue);text-align:center;border:0}
.fbottom{position:absolute;left:140px;right:140px;top:256px;border-top:1px solid #555;padding-top:14px;font-size:10px;display:flex;justify-content:space-between}
</style>
</head>
<body>

<section class="hero" role="img" aria-label="Close-up photo of a fresh salad plate with greens and red onion">
  <div class="topbar">
    <div class="menu-icon"><span></span><span></span><span></span></div>
    <div class="brand"><span class="brand-mark"></span><span class="brand-name">Velmor Plate Kitchen</span></div>
    <div class="top-actions">
      <svg width="16" height="16" viewBox="0 0 16 16"><circle cx="6.5" cy="6.5" r="5" fill="none" stroke="#fff" stroke-width="2"/><path d="M10 10l5 5" stroke="#fff" stroke-width="2"/></svg>
      <span>Cart <svg width="16" height="12" viewBox="0 0 16 12"><path d="M1 1h3l2 8h8l1-6H5" fill="none" stroke="#fff" stroke-width="1.6"/></svg></span>
      <span>Login / Signup</span>
    </div>
  </div>
  <h1 class="hero-title display">Fresh and so Delicious</h1>
  <p class="hero-sub">Lorem Ipsum is simply dummy text of the printing and typesetting industry. Lorem Ipsum has been the industry's standard dummy text ever since the 1500s.</p>
  <span class="btn-yellow">Order Now</span>
  <div class="arrows" style="left:560px;top:560px">
    <svg width="14" height="34" viewBox="0 0 14 34"><path d="M12 2L2 17l10 15" fill="none" stroke="#f1e31c" stroke-width="2.5"/></svg>
    <svg width="14" height="34" viewBox="0 0 14 34"><path d="M2 2l10 15L2 32" fill="none" stroke="#1a9fd8" stroke-width="2.5"/></svg>
  </div>
  <div class="dots" style="left:1132px;top:268px"><i class="on"></i><i></i><i></i><i></i><i></i></div>
</section>

<section class="features">
  <div class="feature">
    <svg width="30" height="30" viewBox="0 0 30 30"><circle cx="15" cy="15" r="12" fill="none" stroke="#f1e31c" stroke-width="2.5"/><circle cx="15" cy="15" r="4" fill="#f1e31c"/></svg>
    <div><strong>Free Shipping</strong><small>Lorem Ipsum is dummy text.</small></div>
  </div>
  <div class="feature mid">
    <svg width="30" height="30" viewBox="0 0 30 30"><circle cx="15" cy="9" r="5" fill="none" stroke="#f1e31c" stroke-width="2.5"/><path d="M5 28c0-7 4-11 10-11s10 4 10 11" fill="none" stroke="#f1e31c" stroke-width="2.5"/></svg>
    <div><strong>Premium Support</strong><small>24/7 Customer service</small></div>
  </div>
  <div class="feature">
    <svg width="40" height="28" viewBox="0 0 40 28"><rect x="2" y="4" width="22" height="16" fill="none" stroke="#f1e31c" stroke-width="2.5"/><path d="M24 9h8l5 6v5H24" fill="none" stroke="#f1e31c" stroke-width="2.5"/><circle cx="10" cy="23" r="3" fill="#f1e31c"/><circle cx="31" cy="23" r="3" fill="#f1e31c"/></svg>
    <div><strong>Payment Method</strong><small>Cash On Delivery</small></div>
  </div>
</section>

<section class="intro">
  <h2 class="section-title display">The Velmor Plan Delivers Diet Meals To Your Door<br>In Toronto, GTA &amp; Montreal</h2>
  <p class="section-lead">Our fresh and delicious diet meals and snacks are made with only the best natural ingredients that nourish your body. Why not let us prepare your meals while you lose the weight?</p>
  <div class="cards">
    <div class="card">
      <svg width="40" height="40" viewBox="0 0 40 40"><path d="M8 34c0-10 4-16 10-18l-2-8 8-2 4 10c6 2 8 8 6 18z" fill="#f1e31c"/></svg>
      <h3>HEALTHY</h3>
      <p>The Velmor Plan is a great way to ensure you are eating all the nutrients you need, and nothing your body doesn't need.</p>
      <span class="more">READ MORE...</span>
    </div>
    <div class="card active">
      <svg width="44" height="40" viewBox="0 0 44 40"><path d="M4 20l12 14L40 4" fill="none" stroke="#1a9fd8" stroke-width="6"/></svg>
      <h3>CHOICE</h3>
      <p>You can choose your own meals from over 100 tasty entrees, desserts and snack foods. You can choose your meals online, or we can select your meals for you.</p>
      <span class="more">READ MORE...</span>
    </div>
    <div class="card">
      <svg width="40" height="40" viewBox="0 0 40 40"><path d="M10 32C10 16 20 8 32 8c0 14-8 22-22 24z" fill="#f1e31c"/></svg>
      <h3>FRESH</h3>
      <p>All of our meals are real food, freshly prepared by our in-house expert chefs.</p>
      <span class="more">READ MORE...</span>
    </div>
    <div class="card">
      <svg width="40" height="40" viewBox="0 0 40 40" fill="none" stroke="#f1e31c" stroke-width="3"><circle cx="20" cy="12" r="6"/><circle cx="11" cy="27" r="6"/><circle cx="29" cy="27" r="6"/></svg>
      <h3>CUSTOMIZE</h3>
      <p>Your meals will be delivered fresh to your door, customized for your unique body type and level of activity.</p>
      <span class="more">READ MORE...</span>
    </div>
  </div>
</section>

<section class="menu">
  <h2 class="section-title display">Select From Over 100 Menu Items</h2>
  <p class="section-lead">You can choose your own meals from over 100 tasty entrees, desserts and snack foods. You can choose your meals online, or we can select your meals for you.</p>
  <div class="dishes">
    <div class="dish dish-d" role="img" aria-label="Photo of plated dinner dishes on a table"><div class="label"><b>Dinner</b><span>Flat Iron Steak With<br>Roasted Vegetables</span></div></div>
    <div class="dish dish-b" role="img" aria-label="Photo of a breakfast plate with eggs"><div class="label"><b>Breakfast</b><span>Mushroom Frittata</span></div></div>
    <div class="dish dish-l" role="img" aria-label="Photo of a fresh lunch salad"><div class="label"><b>Lunch</b><span>Grilled Beef Wrap<br>&amp; Goat Cheese Salad</span></div></div>
    <div class="dish dish-s" role="img" aria-label="Photo of mixed fresh berries"><div class="label"><b>Snack</b><span>Fresh Fruit With Cottage<br>Cheese</span><br>
      <svg width="26" height="26" viewBox="0 0 26 26" style="margin-top:8px"><circle cx="11" cy="11" r="8" fill="none" stroke="#fff" stroke-width="2"/><path d="M17 17l7 7M11 7v8M7 11h8" stroke="#fff" stroke-width="2"/></svg></div></div>
  </div>
  <svg class="slide-arrow" style="left:44px" width="14" height="34" viewBox="0 0 14 34"><path d="M12 2L2 17l10 15" fill="none" stroke="#1a9fd8" stroke-width="2.5"/></svg>
  <svg class="slide-arrow" style="left:1140px" width="14" height="34" viewBox="0 0 14 34"><path d="M2 2l10 15L2 32" fill="none" stroke="#1a9fd8" stroke-width="2.5"/></svg>
</section>

<section class="plan">
  <h2 class="section-title display">The Velmor Plan</h2>
  <p class="section-lead">Real foods designed by nature prepared by Velmor.</p>
  <div class="faq">
    <div class="faq-item"><h4>WHAT YOU GET</h4><p>Velmor Plan Delivery provides you with 3 fresh daily meals and 3 snacks delivered to your doorstep before 6am.</p></div>
    <div class="faq-item"><h4>SELECTION</h4><p>Choose your meals from over 100 delicious entrees, snacks and desserts.</p></div>
    <div class="faq-item"><h4>LUXURY</h4><p>Enjoy the luxury of having your own personal chef and nutritionist prepare Velmor Plan meals for you.</p></div>
    <div class="faq-item"><h4>WHAT IS PHASE 1?</h4><p>Phase 1 is the stricter phase that eliminates bad carbs and processed foods; no sugar, candy, pasta or bread.</p></div>
    <div class="faq-item" style="border:0"><h4>WHAT IS PHASE 2?</h4><p>Phase 2 reintroduces certain healthy carbs into your diet - whole grains, rice and potatoes, providing you with a greater variety of meals.</p></div>
  </div>
  <div class="veg" role="img" aria-label="Illustration of fresh vegetables: peppers, tomatoes, eggplant, garlic and onion"></div>
</section>

<section class="reviews" role="img" aria-label="Dark blurred food photo behind a client testimonial">
  <h2 class="section-title display">What Clients Say`s</h2>
  <span class="quote-mark">&ldquo;</span>
  <p class="quote">Ok, so you know I loved Velmor food the first time but somehow, the second time I love it even more. My lentil soup was incredible! And I am loooving these huge snacks - melba, cheese, veggies, turkey pepperoni - I feel like I am able to graze all day log! So brilliant!</p>
  <p class="author display">Dana</p>
  <div class="arrows" style="left:560px;top:330px">
    <svg width="14" height="34" viewBox="0 0 14 34"><path d="M12 2L2 17l10 15" fill="none" stroke="#f1e31c" stroke-width="2.5"/></svg>
    <svg width="14" height="34" viewBox="0 0 14 34"><path d="M2 2l10 15L2 32" fill="none" stroke="#1a9fd8" stroke-width="2.5"/></svg>
  </div>
  <div class="dots" style="left:1132px;top:170px"><i class="on"></i><i></i><i></i><i></i><i></i></div>
</section>

<section class="newsletter">
  <h2 class="section-title display">The Velmor Plan Is Based On Real Foods Made With<br>Fresh And Natural Ingredients.</h2>
  <p class="section-lead">It's about eating the foods you love and emphasizing the ones that nourish your body; generous portions of fresh fruit, vegetables, meat, fish, nuts and seeds, with smaller servings of grains and dairy.</p>
  <div class="signup"><div class="field">E-Mail Address</div><span class="btn-yellow">Signup</span></div>
</section>

<footer class="footer">
  <div class="fcol" style="left:140px"><h5>Quick Link</h5>Home<br>Velmor Meal Plans<br>Menu<br>Pricing<br>About<br>Press<br>Contact</div>
  <div class="fcol" style="left:364px"><h5>Stay In Touch</h5>
    <div class="contact-row"><svg width="14" height="14" viewBox="0 0 14 14"><path d="M3 1l3 3-2 2c1 2 2 3 4 4l2-2 3 3-2 2C6 13 1 8 1 3z" fill="#f1e31c"/></svg>416-555-0182</div>
    <div class="contact-row"><svg width="14" height="10" viewBox="0 0 14 10"><rect width="14" height="10" fill="#f1e31c"/><path d="M0 0l7 6 7-6" fill="none" stroke="#2a2522"/></svg>sales@velmorplatekitchen.com</div>
    <div class="social"><i></i><i></i><i></i></div>
    <div class="like"><i></i><i></i></div>
  </div>
  <div class="fcol about"><h5>What Is Velmor?</h5>Velmor is the Toronto &amp; Montreal Diet Delivery program based on the Velmor Plan, healthy carbs and the right fats.<br>We provide you with 3 fresh meals, 2 snacks and a dessert delivered to your door before 6am.<br>Try our Velmor Plan delivery plan and start weight loss now!</div>
  <div class="fcol" style="left:893px;top:60px"><h5>Quick Contact</h5>
    <div class="qform"><div>Name</div><div>E-Mail</div><div class="msg">Massage</div><div class="send">SEND</div></div>
  </div>
  <div class="fbottom"><span>© Copyright 2018 Velmor Plate Kitchen - * Individual</span><span>Privacy Policy · Terms &amp; conditions</span></div>
</footer>

</body>
</html>
```